Surface Protection company needs cards

We are a New Zealand company that will apply nanotechnology coatings on surfaces to prevent growth and spread of bacteria, viruses, mold etc with a sprayer. We deal with large corporates, airlines, hospitals and schools so we are after a new modern, simple and clean look that will have great visual impact.
We a company that is focused on prevention and protection.

Company name, Vela Shield

Subtext, Antimicrobial Surface Protection

Logo, VS

Target Market(s)

Hospitals, Transport agencies, Airlines, Corporate entities

Contact Information for Business Card

Company name, VelaShield
Logo, VS

Gareth Tolley
velashieldnz@postbox.example
+64219305562
www.velashield.example.nz

Requirements
Must have
• Simple clean look.
Nice to have
• We apply nano coatings so try and incorporate this into a theme somehow

```html
<!DOCTYPE html>
<html lang="en">
<head>
<meta charset="utf-8">
<title>VelaShield Business Cards</title>
<link rel="stylesheet" href="https://fonts.googleapis.com/css2?family=Open+Sans:wght@600&family=Roboto:wght@400&family=Ubuntu:wght@500;700&display=swap">
<style>
  :root {
    --navy: #262262;
    --paper: #ffffff;
    --ink: #111111;
    --lattice-grey: #e4e4e4;
    --backdrop: #1b1b1b;
  }
  * { box-sizing: border-box; margin: 0; padding: 0; }
  html, body {
    width: 1200px; height: 900px; overflow: hidden;
    background: var(--backdrop);
  }
  .canvas { position: relative; width: 1200px; height: 900px; }
  .card {
    position: absolute; left: 320px;
    width: 560px; height: 320px;
    background: var(--paper);
    border-radius: 20px;
    overflow: hidden;
  }
  .card--front { top: 110px; }
  .card--back { top: 470px; }

  /* front */
  .front__band {
    position: absolute; left: 0; top: 0; width: 100%; height: 34px;
    background: var(--navy);
  }
  .front__tab {
    position: absolute; left: 0; top: 0; width: 190px; height: 72px;
    background: var(--navy);
    clip-path: polygon(0 0, 100% 0, 100% 48%, 86% 100%, 0 100%);
    display: flex; align-items: center; padding-left: 24px;
  }
  .front__brand {
    font-family: "Ubuntu", sans-serif; font-weight: 500;
    font-size: 22px; color: var(--paper);
  }
  .front__tagline {
    position: absolute; right: 26px; top: 8px;
    font-family: "Ubuntu", sans-serif; font-weight: 700;
    font-size: 14px; color: var(--paper); letter-spacing: 0.2px;
  }
  .front__lattice {
    position: absolute; left: 18px; top: 104px;
    width: 118px; height: 108px;
    background: var(--lattice-grey); border-radius: 10px;
  }
  .front__name {
    position: absolute; left: 156px; top: 108px;
    font-family: "Open Sans", sans-serif; font-weight: 600;
    font-size: 36px; line-height: 1.2; color: var(--ink);
    white-space: nowrap;
  }
  .front__rule {
    position: absolute; left: 258px; top: 178px;
    width: 4px; height: 116px; background: var(--navy); border-radius: 2px;
  }
  .contacts {
    position: absolute; left: 276px; top: 184px;
    list-style: none; display: flex; flex-direction: column; gap: 14px;
  }
  .contacts__item {
    display: flex; align-items: center; gap: 10px;
    font-family: "Roboto", sans-serif; font-size: 15px; color: var(--ink);
    white-space: nowrap;
  }
  .contacts__icon {
    flex: none;
    width: 26px; height: 26px; border-radius: 50%;
    background: var(--navy);
    display: flex; align-items: center; justify-content: center;
  }

  /* back */
  .back__art { position: absolute; inset: 0; }
  .back__brand {
    position: absolute; right: 48px; bottom: 72px;
    font-family: "Ubuntu", sans-serif; font-weight: 500;
    font-size: 44px; color: var(--navy);
  }
</style>
</head>
<body>
<main class="canvas">

  <section class="card card--front" aria-label="Business card front">
    <div class="front__band"></div>
    <div class="front__tab"><span class="front__brand">VelaShield</span></div>
    <p class="front__tagline">Antimicrobial Surface Protection</p>
    <div class="front__lattice" role="img" aria-label="Faint grey nano-lattice hexagon motif"></div>
    <h1 class="front__name">Gareth Tolley</h1>
    <div class="front__rule"></div>
    <ul class="contacts">
      <li class="contacts__item">
        <span class="contacts__icon">
          <svg width="16" height="16" viewBox="0 0 16 16" fill="none" stroke="#fff" stroke-width="1.2">
            <circle cx="8" cy="8" r="6.5"/><ellipse cx="8" cy="8" rx="3" ry="6.5"/><line x1="1.5" y1="8" x2="14.5" y2="8"/>
          </svg>
        </span>
        www.velashield.example.nz
      </li>
      <li class="contacts__item">
        <span class="contacts__icon">
          <svg width="14" height="14" viewBox="0 0 16 16" fill="#fff">
            <path d="M3.5 1.5l2.5 0 1 3.5-1.8 1.2a8 8 0 0 0 4.6 4.6l1.2-1.8 3.5 1v2.5a1.5 1.5 0 0 1-1.6 1.5A12 12 0 0 1 2 3.1 1.5 1.5 0 0 1 3.5 1.5z"/>
          </svg>
        </span>
        +64219305562
      </li>
      <li class="contacts__item">
        <span class="contacts__icon">
          <svg width="15" height="15" viewBox="0 0 16 16" fill="none" stroke="#fff" stroke-width="1.3">
            <rect x="1.5" y="3.5" width="13" height="9" rx="1"/><polyline points="1.5,3.5 8,9 14.5,3.5"/>
          </svg>
        </span>
        velashieldnz@postbox.example
      </li>
    </ul>
  </section>

  <section class="card card--back" aria-label="Business card back">
    <svg class="back__art" width="560" height="320" viewBox="0 0 560 320">
      <defs>
        <linearGradient id="lattice-tone" x1="0" y1="0" x2="1" y2="1">
          <stop offset="0" stop-color="#4a4694"/>
          <stop offset="1" stop-color="#34307a"/>
        </linearGradient>
      </defs>
      <polygon points="0,0 560,0 560,95 0,250" fill="#262262"/>
      <rect x="80" y="28" width="220" height="168" rx="14" fill="url(#lattice-tone)" role="img" aria-label="White nano-lattice hexagon motif"/>
    </svg>
    <p class="back__brand">VelaShield</p>
  </section>

</main>
</body>
</html>
```